KRR OutRides

Explain what KRR means ( Keel, Rudder, Ripple Journey)
We offer surfing, wake baording, water skliing on a state of the art surf and equipment all included in the charter. The captain is a NBH Harbor Patrol captain.
We offer wake surfing, wakeboarding, water skiing, tubing. We have state of the art video with 3 cameras onboard 2,360 view camers for videioing your day on the water.
Located on the Delta, serving Lake Tahoe in the summer time, Lake Berryasea, and other local lakes.
We specliaize in birthday parties, bacholer, bachlorrete, graduation parties and team building events.

Target Market(s)

Indivuals, business, wedding and event planners

Industry/Entity Type

Water sports

Requirements
Must have
• My logo,
Nice to have
• Simple, not to busy

```html
<!DOCTYPE html>
<html lang="en">
<head>
<meta charset="utf-8">
<title>KRR OutRides – Flyer</title>
<link href="https://fonts.googleapis.com/css2?family=Montserrat:wght@500;600;700;800;900&display=swap" rel="stylesheet">
<style>
  :root{
    --navy:#0c2a5c;
    --blue:#1e88e5;
    --sky:#3aa9f0;
    --aqua:#8fd3ff;
    --ink:#0b0b0b;
    --white:#ffffff;
    --pale:#eef6fd;
  }
  *{box-sizing:border-box;margin:0;padding:0}
  html,body{width:849px;height:1200px;overflow:hidden;background:#fff}
  body{font-family:"Montserrat",Arial,sans-serif;color:var(--ink)}
  .flyer{position:relative;width:849px;height:1200px;overflow:hidden;
    background:radial-gradient(ellipse at 20% 30%,var(--pale) 0%,#fff 55%),#fff}
  .backdrop-pattern{position:absolute;inset:0;
    background:linear-gradient(160deg,rgba(143,211,255,.18),rgba(255,255,255,0) 45%,rgba(143,211,255,.16) 80%)}

  .brand{position:absolute;top:48px;left:0;width:100%;display:flex;justify-content:center;align-items:center;gap:14px}
  .brand-dot{width:28px;height:28px;border-radius:50%;background:var(--navy)}
  .brand-name{font-size:52px;font-weight:800;color:var(--navy);letter-spacing:1px}
  .brand-meaning{position:absolute;top:128px;width:100%;text-align:center;
    font-size:20px;font-weight:700;color:var(--blue);letter-spacing:.5px}

  .tagline{position:absolute;top:222px;width:100%;text-align:center;
    font-size:33px;font-weight:800;color:var(--navy);letter-spacing:.5px}

  .splash{position:absolute;border-radius:50% 50% 45% 55% / 60% 40% 60% 40%;
    background:linear-gradient(135deg,var(--aqua),var(--blue))}
  .splash-top{left:40px;top:290px;width:260px;height:100px;transform:rotate(-8deg)}
  .splash-right{left:640px;top:660px;width:180px;height:70px;transform:rotate(10deg)}

  .offer-box{position:absolute;left:62px;top:462px;width:378px;height:350px;
    background:var(--ink);color:var(--white);padding:26px 28px}
  .offer-title{font-size:40px;font-weight:800;line-height:1.05}
  .offer-list{list-style:none;margin-top:16px;font-size:18px;font-weight:600;line-height:1.28}
  .offer-list li{position:relative;padding-left:30px;margin-bottom:7px}
  .offer-list li::before{content:"✱";position:absolute;left:0;top:0;color:var(--sky);font-size:17px}
  .accent{color:var(--sky)}

  .memorable-box{position:absolute;left:470px;top:400px;width:350px;height:240px;
    background:var(--blue);border-radius:22px;padding:24px 26px;text-align:center}
  .memorable-title{font-size:24px;font-weight:800;color:var(--ink);line-height:1.15}
  .memorable-text{margin-top:14px;font-size:17px;font-weight:600;color:var(--white);line-height:1.35}

  .photo-band{position:absolute;left:-20px;top:850px;width:900px;height:120px;
    background:var(--blue);transform:rotate(-5deg)}
  .photo-strip{position:absolute;left:10px;top:810px;width:830px;height:200px;
    display:flex;gap:10px;align-items:center;transform:rotate(-5deg)}
  .photo{flex:1;height:175px;border:4px solid #fff}
  .photo:nth-child(1){background:linear-gradient(160deg,#b9dff5,#2e7fb8)}
  .photo:nth-child(2){background:linear-gradient(160deg,#59c1e8,#1d6b45)}
  .photo:nth-child(3){background:linear-gradient(160deg,#f1d3b0,#2f6aa0)}
  .photo:nth-child(4){background:linear-gradient(160deg,#d8ecf7,#3a86c0)}
  .photo:nth-child(5){background:linear-gradient(160deg,#8ac7ec,#1b4f86)}
  .photo:nth-child(6){background:linear-gradient(160deg,#c8e7f7,#2b7cb9)}

  .location{position:absolute;left:62px;top:1050px;width:340px;display:flex;gap:10px;
    font-size:17px;font-weight:700;line-height:1.3;color:var(--navy)}
  .location svg{flex:none;margin-top:2px}

  .specialty{position:absolute;left:467px;top:1020px;width:350px}
  .specialty-label{display:inline-block;background:var(--blue);color:var(--white);
    font-size:19px;font-weight:800;padding:5px 14px}
  .specialty-text{margin-top:8px;font-size:17px;font-weight:700;line-height:1.3;color:var(--navy)}

  .wave-corner{position:absolute;bottom:0;left:0}
</style>
</head>
<body>
<main class="flyer">
  <div class="backdrop-pattern" role="img" aria-label="Faint light blue water pattern background"></div>

  <header class="brand">
    <span class="brand-dot"></span>
    <span class="brand-name">KRR OutRides</span>
  </header>
  <p class="brand-meaning">Keel, Rudder, Ripple Journey</p>

  <h1 class="tagline">SURF IT, LAUNCH IT, CARVE IT!</h1>

  <div class="splash splash-top" role="img" aria-label="Blue water splash illustration"></div>
  <div class="splash splash-right" role="img" aria-label="Blue water splash illustration"></div>

  <section class="memorable-box">
    <h2 class="memorable-title">To make your<br>Experience more<br>Memorable</h2>
    <p class="memorable-text">We have state of the art video with 3 cameras onboard 2,360 view cameras for videoing your day on the water.</p>
  </section>

  <section class="offer-box">
    <h2 class="offer-title">WHAT WE<br>OFFER</h2>
    <ul class="offer-list">
      <li>Wake Surfing</li>
      <li>Wake Boarding</li>
      <li>Water Skiing</li>
      <li>Tubing on a state of the <span class="accent">Art Surf,</span> equipment all included in the charter.</li>
      <li>Highly experienced <span class="accent">NBH Harbor Patrol Captain.</span></li>
    </ul>
  </section>

  <div class="photo-band"></div>
  <div class="photo-strip">
    <div class="photo" role="img" aria-label="Photo of a wake surfer on a lake"></div>
    <div class="photo" role="img" aria-label="Photo of a tropical shoreline with palm trees"></div>
    <div class="photo" role="img" aria-label="Photo of mountains above a lake"></div>
    <div class="photo" role="img" aria-label="Photo of a water skier"></div>
    <div class="photo" role="img" aria-label="Photo of a wakeboarder jumping"></div>
    <div class="photo" role="img" aria-label="Photo of a surfer riding a wave"></div>
  </div>

  <p class="location">
    <svg width="20" height="26" viewBox="0 0 20 26" aria-hidden="true"><path d="M10 0C4.5 0 0 4.4 0 9.8 0 17 10 26 10 26s10-9 10-16.2C20 4.4 15.5 0 10 0z" fill="#1e88e5"/><circle cx="10" cy="9.5" r="3.6" fill="#fff"/></svg>
    <span>Delta, serving Lake Tahoe in the summer time, Lake Berryessa, &amp; other local lakes.</span>
  </p>

  <section class="specialty">
    <span class="specialty-label">WE SPECIALIZE IN</span>
    <p class="specialty-text">Birthday Parties, Bachelor, Bachlorette, Graduation Parties &amp; Team Building Events.</p>
  </section>

  <svg class="wave-corner" width="849" height="50" viewBox="0 0 849 50" aria-hidden="true">
    <path d="M0 20 C120 0 220 40 340 28 C390 24 420 36 440 50 L0 50Z" fill="#1e88e5"/>
    <path d="M849 30 C790 20 740 42 700 50 L849 50Z" fill="#8fd3ff"/>
  </svg>
</main>
</body>
</html>
```